Eye-catching & Glamorous Labels for Skincare Bottles & Jars

We need new labels designed for our product range as we have been dormant for a few years and are now rebranding Velora Grace - Kindly Made Skincare. The label sizes are defined in the attached word document. All products have either a bright silver or a matte silver lid pump/spray so please keep this in mind.

We are open to colours and invite you to create bright trendy labels which are coordinated with the logo attached. The logo is not of any specific colour so dark on light, light on dark, tone on tone - we like purple / duck egg blue / turquoise WITH matte silver, however stronger colours like navy plus maroon with matte silver is also a strong favourite. If you feel inspired by a colour you think would be appropriate to Velora Grace please feel free to have a go.

A front section for product information is required and the back should include relevant details ie ingredients, company info, and a note that there has been no testing on animals.

The serum bottle will require a front and back label on a clear label in a pale colour to coordinate with the rest of the range. Size for this label is 35mm top edge, 25mm bottom edge, height 45mm - I have attached a picture of the serum bottle as they were originally pad printed. Please don't hesitate to contact me for any further information. Good luck!

Target Market(s)

Educated professional women 30-45 who are regular skincare users and looking for beautiful skincare products without animal derived ingredients and animal testing

Industry/Entity Type

Skin Care Product

Font styles to use
Serif
Sans Serif
Decorative
Script

Colors

Designer to choose colors to be used in the design.

Requirements
Must have
• Velora Grace Logo - eye catching design - not too busy or cramped.
Nice to have
• Is it possible to create a background pattern using a very small image of the logo? Just a thought.

```html
<!DOCTYPE html>
<html lang="en">
<head>
<meta charset="utf-8">
<title>Velora Grace – Timeless Glow Line Labels</title>
<link href="https://fonts.googleapis.com/css2?family=Oswald:wght@600&family=Arimo:wght@400;700&family=Great+Vibes&display=swap" rel="stylesheet">
<style>
  :root{
    --canvas:#7b7b7b;
    --ink:#111111;
    --paper:#f4f4f4;
    --paper-shade:#d9d9d9;
    --purple:#8a1a6e;
    --purple-soft:#c690b8;
    --teal:#3ab3c3;
    --teal-soft:#a6dde4;
    --white:#ffffff;
  }
  *{box-sizing:border-box;margin:0;padding:0}
  html,body{width:1200px;height:1200px;overflow:hidden}
  body{background:var(--canvas);position:relative;font-family:"Arimo",Arial,sans-serif;color:var(--ink)}

  .is-purple{--accent:var(--purple);--accent-soft:var(--purple-soft)}
  .is-teal{--accent:var(--teal);--accent-soft:var(--teal-soft)}

  .label{position:absolute;overflow:hidden;background:linear-gradient(100deg,var(--paper-shade),var(--paper) 30%,var(--white) 55%,var(--paper) 80%,var(--paper-shade))}
  .brand-band{background:var(--ink);display:flex;flex-direction:column;align-items:center}
  .brand-disc{background:var(--white);border-radius:50%;display:flex;align-items:center;justify-content:center;text-align:center;font-weight:700;color:var(--ink);line-height:1.05}
  .brand-name{font-family:"Oswald",Arial,sans-serif;font-weight:600;color:var(--accent);letter-spacing:.5px;line-height:1;text-transform:uppercase}
  .brand-tag{color:var(--accent);border-bottom:1px solid var(--accent);text-transform:uppercase;letter-spacing:.3px;white-space:nowrap}
  .info{display:flex;flex-direction:column;align-items:center;text-align:center;position:relative;z-index:2}
  .range-title{font-family:"Great Vibes",cursive;color:var(--ink);line-height:1;white-space:nowrap}
  .product-line{display:flex;align-items:center;gap:5px;color:var(--accent);font-weight:700;white-space:nowrap}
  .product-line::before,.product-line::after{content:"";height:1.5px;background:var(--ink);display:block}
  .product-name::before,.product-name::after{content:"•";color:var(--ink);margin:0 3px}
  .note{text-transform:uppercase;color:#222;white-space:nowrap}
  .volume{background:var(--ink);color:var(--white);border-radius:50%;display:flex;align-items:center;justify-content:center;font-weight:700}
  .flower{position:absolute;background:radial-gradient(ellipse at 50% 90%,var(--accent) 0%,var(--accent) 35%,var(--accent-soft) 60%,transparent 72%)}

  /* flat box labels */
  .flat-label{top:19px;width:494px;height:246px}
  .flat-label.left{left:78px}
  .flat-label.right{left:622px}
  .flat-label .brand-band{height:122px;padding-top:9px}
  .flat-label .brand-disc{width:48px;height:48px;font-size:7.5px}
  .flat-label .brand-name{font-size:27px;margin-top:8px}
  .flat-label .brand-tag{font-size:12px;padding:2px 14px 1px;margin-top:2px;color:var(--white)}
  .flat-label.is-teal .brand-tag{color:var(--accent)}
  .flat-label .info{padding-top:6px}
  .flat-label .range-title{font-size:23px}
  .flat-label .product-line{font-size:14px;margin-top:3px}
  .flat-label .product-line::before,.flat-label .product-line::after{width:48px}
  .flat-label .note{font-size:10px;margin-top:5px}
  .flat-label .note + .note{margin-top:4px}
  .flat-label .volume{width:32px;height:32px;font-size:11px;margin-top:6px}
  .flat-label .flower{left:-20px;bottom:-12px;width:135px;height:110px}
  .flat-label .edge-arc{position:absolute;right:-40px;top:122px;width:60px;height:124px;border-radius:50%;background:var(--accent)}

  /* bottle front labels */
  .bottle-label{top:708px;width:306px;height:426px;clip-path:polygon(0 0,100% 0,86% 100%,14% 100%)}
  .bottle-label.one{left:78px}
  .bottle-label.two{left:444px}
  .bottle-label.three{left:806px}
  .bottle-label .brand-band{height:172px;padding-top:30px}
  .bottle-label .brand-disc{width:70px;height:70px;font-size:10px}
  .bottle-label .brand-name{font-size:29px;margin-top:13px}
  .bottle-label .brand-tag{font-size:13px;font-weight:700;padding:2px 12px 3px;margin-top:3px}
  .bottle-label .info{padding-top:12px}
  .bottle-label .range-title{font-size:28px}
  .bottle-label .product-line{font-size:14.5px;margin-top:6px}
  .bottle-label .product-line::before,.bottle-label .product-line::after{width:34px}
  .bottle-label .note{font-size:11px;margin-top:9px}
  .bottle-label .note.ritual{font-size:13px;margin-top:8px}
  .bottle-label .volume{width:42px;height:42px;font-size:12px;margin-top:13px}
  .bottle-label .flower{left:50%;transform:translateX(-50%);bottom:0;width:130px;height:72px}
</style>
</head>
<body>

  <section class="label flat-label left is-purple">
    <header class="brand-band">
      <div class="brand-disc">VELORA<br>GRACE</div>
      <h1 class="brand-name">Velora Grace</h1>
      <p class="brand-tag">Kindly Made Skincare</p>
    </header>
    <div class="info">
      <p class="range-title">Timeless Glow Line</p>
      <p class="product-line"><span class="product-name">Facial Scrub</span></p>
      <p class="note">Silken Ritual</p>
      <p class="note">There has been no testing on animals</p>
      <div class="volume">30ml</div>
    </div>
    <div class="flower" role="img" aria-label="Purple lotus flower illustration"></div>
    <div class="edge-arc"></div>
  </section>

  <section class="label flat-label right is-teal">
    <header class="brand-band">
      <div class="brand-disc">VELORA<br>GRACE</div>
      <h1 class="brand-name">Velora Grace</h1>
      <p class="brand-tag">Kindly Made Skincare</p>
    </header>
    <div class="info">
      <p class="range-title">Timeless Glow Line</p>
      <p class="product-line"><span class="product-name">Facial Scrub</span></p>
      <p class="note">Silken Ritual</p>
      <p class="note">There has been no testing on animals</p>
      <div class="volume">30ml</div>
    </div>
    <div class="flower" role="img" aria-label="Turquoise lotus flower illustration"></div>
    <div class="edge-arc"></div>
  </section>

  <section class="label bottle-label one is-teal">
    <header class="brand-band">
      <div class="brand-disc">VELORA<br>GRACE</div>
      <h2 class="brand-name">Velora Grace</h2>
      <p class="brand-tag">Kindly Made Skincare</p>
    </header>
    <div class="info">
      <p class="range-title">Timeless Glow Line</p>
      <p class="product-line"><span class="product-name">OIL SERUM</span></p>
      <p class="note ritual">Silken Ritual</p>
      <p class="note">There has been no testing on animals</p>
      <div class="volume">30ml</div>
    </div>
    <div class="flower" role="img" aria-label="Turquoise lotus flower illustration"></div>
  </section>

  <section class="label bottle-label two is-purple">
    <header class="brand-band">
      <div class="brand-disc">VELORA<br>GRACE</div>
      <h2 class="brand-name">Velora Grace</h2>
      <p class="brand-tag">Kindly Made Skincare</p>
    </header>
    <div class="info">
      <p class="range-title">Timeless Glow Line</p>
      <p class="product-line"><span class="product-name">TONER &amp; CLEANSER</span></p>
      <p class="note ritual">Silken Ritual</p>
      <p class="note">There has been no testing on animals</p>
      <div class="volume">30ml</div>
    </div>
    <div class="flower" role="img" aria-label="Purple lotus flower illustration"></div>
  </section>

  <section class="label bottle-label three is-teal">
    <header class="brand-band">
      <div class="brand-disc">VELORA<br>GRACE</div>
      <h2 class="brand-name">Velora Grace</h2>
      <p class="brand-tag">Kindly Made Skincare</p>
    </header>
    <div class="info">
      <p class="range-title">Timeless Glow Line</p>
      <p class="product-line"><span class="product-name">Day Cream &amp; Night Cream</span></p>
      <p class="note ritual">Silken Ritual</p>
      <p class="note">There has been no testing on animals</p>
      <div class="volume">30ml</div>
    </div>
    <div class="flower" role="img" aria-label="Turquoise lotus flower illustration"></div>
  </section>

</body>
</html>
```